Design our industrial business landing pages

Welcome!

We have five landing pages that follow a very similar structure that I need fresh designs submitted for.

I have uploaded all of the files for entries to view and have made a structure for how I want the designs to generally look but PLEASE get CREATIVE.

I have made a short video to explain the project, please also view the google docs.

VIDEO

https://www.clipvane.com/share/a4f19c2e7b0d4e6f8a3c5d7e9b1f2a60?sid=f3b8d1e2-6a4c-4f7e-9b2d-1c5e8a7f3d90

OLD WEBSITE - https://www.marlowfield-pvc-solutions.co.uk/

DOCUMENT - https://docs.papernook.com/document/d/7kTq2Wx9LmPz4Rv8Ns3Bc6Yh1Jf5Gd0Ue2Ai4Oo7Xe/edit?usp=sharing

No one is following the design brief I set. All designers need to refer to this document. Not a single designer has followed this brief https://docs.papernook.com/document/d/7kTq2Wx9LmPz4Rv8Ns3Bc6Yh1Jf5Gd0Ue2Ai4Oo7Xe/edit?usp=sharing

```html
<!DOCTYPE html>
<html lang="en">
<head>
<meta charset="utf-8">
<title>Marlowfield's – Landing Page Mobile View</title>
<link href="https://fonts.googleapis.com/css2?family=Montserrat:wght@400;500;600;700;800&display=swap" rel="stylesheet">
<style>
:root{
  --navy:#13365a;
  --navy-deep:#0f2c4a;
  --steel:#2f5d7e;
  --slate-bg:#c9d6e0;
  --panel-white:#ffffff;
  --light:#eef3f7;
  --red:#c8334a;
  --red-soft:#d5485d;
  --red-ring:#f2b8c1;
  --blue-text:#2f6fa3;
  --title-blue:#3b6f95;
  --muted:#c3d2df;
}
*{box-sizing:border-box;margin:0;padding:0}
html,body{width:1200px;height:771px;overflow:hidden}
body{font-family:"Montserrat",sans-serif;background:var(--slate-bg);position:relative}
.abs{position:absolute}
svg.ico{display:block;fill:none;stroke:#fff;stroke-width:1.5;stroke-linecap:round;stroke-linejoin:round}

/* left intro panel */
.intro{left:0;top:0;width:247px;height:771px;background:var(--panel-white)}
.intro-title{left:28px;top:142px;font-size:28px;font-weight:700;color:var(--title-blue)}
.intro-sub{left:28px;top:188px;font-size:19px;line-height:27px;color:var(--title-blue);font-weight:400}
.intro-sub span{display:block}
.intro-sub span+span{padding-left:5px}
.intro-base{left:0;top:450px;width:247px;height:321px;background:var(--navy-deep);border-radius:18px 18px 0 0}
.intro-mark{left:86px;top:406px;width:78px;height:67px;background:var(--steel)}

/* footer screen */
.screen{overflow:hidden}
.footer-screen{left:286px;top:0;width:252px;height:314px;border-radius:0 0 22px 22px;
  background:linear-gradient(180deg,#3a6a8c 0%,#24506f 60%,#1b3e5a 100%);color:#fff;text-align:center;
  box-shadow:0 4px 10px rgba(15,44,74,.35)}
.footer-address{margin-top:2px;font-size:8.5px;line-height:11px;color:#dbe6ef}
.footer-heading{font-size:11.5px;font-weight:600;letter-spacing:.5px;margin-top:12px}
.footer-links{list-style:none;font-size:8.5px;line-height:11.8px;color:#dbe6ef;margin-top:6px}
.footer-rule{height:1px;background:rgba(255,255,255,.35);margin:22px 0 8px}
.footer-copy{font-size:8px;line-height:12px;color:#dbe6ef}
.footer-copy b{color:var(--red-soft);font-weight:500}

/* home screen */
.home-screen{left:286px;top:344px;width:252px;height:440px;border-radius:22px 22px 0 0;background:#fff;
  box-shadow:0 -2px 10px rgba(15,44,74,.25)}
.home-header{height:66px;display:flex;align-items:center;justify-content:space-between;padding:0 16px 0 14px}
.brand{display:flex;align-items:center;gap:6px;font-size:11px;font-weight:700;color:var(--navy)}
.brand-dot{width:24px;height:24px;border-radius:50%;background:var(--navy)}
.menu-icon{width:20px}
.hero{position:relative;height:290px;background:linear-gradient(180deg,#2d3a33 0%,#3f5248 45%,#5b7386 100%);color:#fff;text-align:center}
.hero h1{position:absolute;top:54px;left:0;right:0;font-size:18px;font-weight:800;letter-spacing:.6px}
.hero p{position:absolute;top:84px;left:24px;right:24px;font-size:10px;line-height:13px;color:#eef2f5}
.hero-btn{position:absolute;left:104px;top:178px;width:74px;height:32px;border-radius:16px;background:var(--red);font-size:8.5px;line-height:32px;color:#fff}
.trusted{text-align:center;margin-top:24px;font-size:17px;font-weight:800;color:var(--navy);line-height:22px}
.trusted em{font-style:normal;color:var(--red)}

/* middle screen */
.mid-screen{left:597px;top:0;width:257px;height:771px;background:var(--navy);color:#fff}
.quality-title{text-align:center;margin-top:22px;font-size:12px;font-weight:700;display:flex;justify-content:center;gap:6px;align-items:center}
.feature-row{display:grid;grid-template-columns:106px 96px;justify-content:center;gap:8px;font-size:7.5px;color:var(--muted);margin-top:8px}
.feature-row span{display:flex;align-items:center;gap:4px;white-space:nowrap}
.feature-row svg{stroke:var(--muted);stroke-width:1.2}
.tiles{position:absolute;left:54px;top:94px;display:grid;grid-template-columns:70px 70px;gap:8px}
.tile{height:70px;border:1.5px solid #fff;border-radius:14px;display:flex;flex-direction:column;align-items:center;justify-content:center;gap:6px;font-size:7.5px;text-align:center;line-height:9px}
.tile-icon{width:28px;height:28px;border-radius:50%;background:var(--red);border:1.5px solid #fff;display:flex;align-items:center;justify-content:center}
.strength{position:absolute;left:0;top:265px;width:257px;height:318px;background:var(--navy)}
.strength-band{height:62px;background:#fff;text-align:center;padding-top:22px;font-size:10px;line-height:14px;color:#6b7f92;letter-spacing:.4px}
.strength-band b{display:block;color:var(--blue-text);font-weight:700}
.circle{position:absolute;width:104px;height:104px;border-radius:50%;background:var(--red);border:3px solid var(--red-ring);
  display:flex;flex-direction:column;align-items:center;justify-content:center;text-align:center;font-size:7.5px;line-height:9.5px;padding:0 16px;gap:6px}
.view-more{position:absolute;left:0;right:0;top:283px;display:flex;justify-content:center;align-items:center;gap:6px;font-size:8.5px}
.view-more span{width:16px;height:16px;border-radius:50%;background:#fff;display:flex;align-items:center;justify-content:center}
.mid-rule{position:absolute;left:0;right:0;top:582px;height:1px;background:rgba(255,255,255,.35)}
.badge-circle{position:absolute;left:100px;top:614px;width:58px;height:58px;border-radius:50%;background:#dfe8f0}
.nationwide{position:absolute;top:678px;left:0;right:0;text-align:center;font-size:17px;font-weight:400}
.nationwide b{font-weight:700}
.nationwide-copy{position:absolute;top:708px;left:22px;right:22px;text-align:center;font-size:9.5px;line-height:13px;color:#dbe6ef}

/* right screen */
.right-screen{left:909px;top:0;width:256px;height:771px;background:var(--light)}
.how-title{text-align:center;margin-top:28px;font-size:19px;color:var(--navy);font-weight:500}
.how-title b{font-weight:700}
.timeline{position:absolute;left:19px;top:84px;width:1px;height:332px;background:#9fb2c3}
.step-dot{position:absolute;left:11px;width:17px;height:17px;border-radius:50%;background:var(--navy);color:#fff;font-size:8px;display:flex;align-items:center;justify-content:center}
.step-label{position:absolute;left:38px;font-size:11px;font-weight:700;color:var(--navy)}
.step-card{position:absolute;left:38px;width:182px;border:2px solid var(--red);border-radius:12px;background:#fff}
.step-shot{position:absolute;border-radius:6px;background:linear-gradient(135deg,#dfe9f2,#b9cddd)}
.question{position:absolute;left:38px;top:408px;font-size:10.5px;color:var(--navy);font-weight:500}
.question b{color:var(--blue-text);text-decoration:underline}
.brochure-band{position:absolute;left:0;top:441px;width:256px;height:330px;background:var(--navy);color:#fff;text-align:center}
.brochure-card{position:absolute;left:54px;top:55px;width:144px;height:185px;border:1.5px solid #9fb8cf;border-radius:12px}
.brochure-img{position:absolute;left:16px;top:18px;width:110px;height:120px;background:linear-gradient(180deg,#e6ecf1 0%,#c6d3de 40%,#b4424f 100%)}
.brochure-label{position:absolute;left:0;right:0;top:150px;font-size:7.5px;font-weight:700;letter-spacing:.3px}
.download{position:absolute;top:262px;left:0;right:0;font-size:15px}
.download-title{position:absolute;top:286px;left:0;right:0;font-size:15px;font-weight:700}
.download-copy{position:absolute;top:313px;left:0;right:0;font-size:9.5px;color:#dbe6ef}
.download-copy b{font-style:italic;color:#fff}
</style>
</head>
<body>

<section class="abs intro">
  <h1 class="abs intro-title">Marlowfield's</h1>
  <p class="abs intro-sub"><span>Landing Page</span><span>Mobile View</span></p>
</section>
<div class="abs intro-base"></div>
<div class="abs intro-mark"></div>

<section class="abs screen footer-screen">
  <p class="footer-address">Brookside Industrial Park,<br>Mill Road Brookside<br>Ashgrove AG4 5UW</p>
  <h2 class="footer-heading">QUICK LINKS</h2>
  <ul class="footer-links"><li>Home</li><li>All Products</li><li>About</li><li>Videos</li><li>Brochures &amp; Samples</li></ul>
  <h2 class="footer-heading">SOLUTIONS</h2>
  <ul class="footer-links"><li>Industrial Curtain Wall</li><li>Spray Booth Curtains</li><li>Welding Curtains</li><li>PVC Strip Curtain</li><li>Warehouse Curtains</li></ul>
  <div class="footer-rule"></div>
  <p class="footer-copy">© 2024 by <b>Marlowfield PVC Solutions</b>.<br>All Rights Reserved.</p>
</section>

<section class="abs screen home-screen">
  <header class="home-header">
    <div class="brand"><span class="brand-dot"></span>MARLOWFIELD'S</div>
    <svg class="menu-icon" viewBox="0 0 20 14"><g stroke="#7d8d9c" stroke-width="1.6"><line x1="0" y1="1" x2="20" y2="1"/><line x1="0" y1="7" x2="20" y2="7"/><line x1="0" y1="13" x2="20" y2="13"/></g></svg>
  </header>
  <div class="hero" role="img" aria-label="Photo of clear PVC strip curtains in an industrial warehouse doorway">
    <h1>STRIP CURTAINS</h1>
    <p>Upgrade your industrial space with our durable, flexible Strip Curtains for maximum efficiency and easy installation</p>
    <div class="hero-btn">Book Now</div>
  </div>
  <h2 class="trusted"><em>TRUSTED</em> BY GLOBAL<br>COMPANIES</h2>
</section>

<section class="abs screen mid-screen">
  <h2 class="quality-title">Impeccable Quality
    <svg class="ico" width="12" height="14" viewBox="0 0 12 14"><circle cx="6" cy="5" r="4.3"/><path d="M4 10.5v2.5h4v-2.5"/></svg>
  </h2>
  <div class="feature-row">
    <span><svg class="ico" width="10" height="10" viewBox="0 0 10 10"><path d="M1 3l4-2 4 2-4 2z"/><path d="M1 5.5l4 2 4-2"/><path d="M1 7.5l4 2 4-2"/></svg>Multiple Thicknesses</span>
    <span><svg class="ico" width="10" height="10" viewBox="0 0 10 10"><circle cx="5" cy="5" r="4"/><circle cx="3.5" cy="4" r=".6"/><circle cx="6.5" cy="4" r=".6"/><circle cx="5" cy="6.8" r=".6"/></svg>Various Colours</span>
  </div>
  <div class="feature-row">
    <span><svg class="ico" width="10" height="10" viewBox="0 0 10 10"><path d="M2 8l4-4"/><circle cx="7" cy="3" r="2"/><path d="M1.5 8.5l1 -1"/></svg>Installation Service</span>
    <span><svg class="ico" width="12" height="10" viewBox="0 0 12 10"><rect x="1" y="2" width="6" height="5"/><path d="M7 4h2.5l1.5 2v1H7"/><circle cx="3" cy="8" r="1"/><circle cx="9" cy="8" r="1"/></svg>3 Day Delivery</span>
  </div>
  <div class="tiles">
    <div class="tile"><span class="tile-icon"><svg class="ico" width="14" height="14" viewBox="0 0 14 14"><path d="M7 1l5 2v4c0 3-2.3 5-5 6-2.7-1-5-3-5-6V3z"/><path d="M4.5 7l2 2 3-3.5"/></svg></span>Quality<br>Assured</div>
    <div class="tile"><span class="tile-icon"><svg class="ico" width="14" height="14" viewBox="0 0 14 14"><path d="M7 1.5l1.7 3.4 3.8.5-2.7 2.6.6 3.7L7 10l-3.4 1.7.6-3.7L1.5 5.4l3.8-.5z"/></svg></span>Experienced</div>
    <div class="tile"><span class="tile-icon"><svg class="ico" width="14" height="14" viewBox="0 0 14 14"><path d="M1.5 12.5V6l3.5 2V6l3.5 2V3h3.5v9.5z"/></svg></span>Manufactured<br>by us</div>
    <div class="tile"><span class="tile-icon"><svg class="ico" width="14" height="14" viewBox="0 0 14 14"><circle cx="7" cy="7" r="2"/><path d="M7 1v2M7 11v2M1 7h2M11 7h2M2.8 2.8l1.4 1.4M9.8 9.8l1.4 1.4M2.8 11.2l1.4-1.4M9.8 4.2l1.4-1.4"/></svg></span>Project<br>Management</div>
  </div>

  <div class="strength">
    <div class="strength-band">WHERE INDUSTRIAL STRENGTH<b>MEETS GOING THE EXTRA LENGTH</b></div>
    <div class="circle" style="left:20px;top:78px"><svg class="ico" width="20" height="20" viewBox="0 0 20 20"><path d="M10 2l7 3v5c0 4-3 7-7 8-4-1-7-4-7-8V5z"/><path d="M7 10l2 2 4-4"/></svg>Resists colour contamination</div>
    <div class="circle" style="left:134px;top:78px"><svg class="ico" width="20" height="20" viewBox="0 0 20 20"><circle cx="10" cy="6.5" r="3.5"/><path d="M3.5 18c0-4 3-6.5 6.5-6.5s6.5 2.5 6.5 6.5"/></svg>Protect employees</div>
    <div class="circle" style="left:20px;top:182px"><svg class="ico" width="20" height="20" viewBox="0 0 20 20"><circle cx="10" cy="10.5" r="7"/><path d="M10 6.5v4l3 2"/><path d="M8 2h4"/></svg>Quick to deploy</div>
    <div class="circle" style="left:134px;top:182px"><svg class="ico" width="20" height="20" viewBox="0 0 20 20"><path d="M10 2c1 3.5 5 5.5 5 10a5 5 0 0 1-10 0c0-2.5 1.5-4 2.5-5 .3 1.5 1 2.5 2 3 0-3 .5-5.5.5-8z"/></svg>Fire resistant material options available</div>
    <div class="view-more">View More <span><svg width="8" height="6" viewBox="0 0 8 6"><path d="M1 1l3 3 3-3" fill="none" stroke="#13365a" stroke-width="1.5"/></svg></span></div>
  </div>
  <div class="mid-rule"></div>
  <div class="badge-circle"></div>
  <h2 class="nationwide">We install <b>Nationwide</b></h2>
  <p class="nationwide-copy">We are delighted to introduce ourselves as a reputable, registered limited company based in the beautiful county of</p>
</section>

<section class="abs screen right-screen">
  <h2 class="how-title">How it <b>Works</b></h2>
  <div class="timeline"></div>
  <div class="step-dot" style="top:75px">1</div>
  <p class="step-label" style="top:76px">Supply Only</p>
  <div class="step-card" style="top:97px;height:124px" role="img" aria-label="Preview screens of the supply only ordering steps">
    <div class="step-shot" style="left:10px;top:12px;width:70px;height:46px"></div>
    <div class="step-shot" style="left:90px;top:22px;width:80px;height:56px"></div>
    <div class="step-shot" style="left:20px;top:66px;width:66px;height:44px"></div>
  </div>
  <div class="step-dot" style="top:241px">2</div>
  <p class="step-label" style="top:242px">Fully Installed</p>
  <div class="step-card" style="top:265px;height:132px" role="img" aria-label="Preview screens of the fully installed service steps">
    <div class="step-shot" style="left:12px;top:12px;width:80px;height:50px"></div>
    <div class="step-shot" style="left:100px;top:18px;width:70px;height:50px"></div>
    <div class="step-shot" style="left:28px;top:72px;width:120px;height:46px"></div>
  </div>
  <div class="step-dot" style="top:407px">?</div>
  <p class="question">Have a question? <b>Contact us</b></p>

  <div class="brochure-band">
    <div class="brochure-card">
      <div class="brochure-img" role="img" aria-label="Cover of the full product brochure showing a warehouse with strip curtains"></div>
      <p class="brochure-label">FULL PRODUCT BROCHURE</p>
    </div>
    <p class="download">Download</p>
    <h2 class="download-title">Our Full Product Brochure</h2>
    <p class="download-copy">Our <b>Commitment</b> to maintaining an</p>
  </div>
</section>

</body>
</html>
```